Construction Company

Design a clutter free business card, it can be double-sided utilizing the logo for BDN Ltd simple with all relevant contact information.

Please also a letterhead design to function for the purposes of invoicing, all mail requirements, with header to be distinctive while the footer ties page together and incorporates all necessary information.

For now, please use generic / dummy text and when a winner is selected, I will disclose the contact information.

Hi Designers! Please read the updated brief which includes the design of a business card and letterhead. Thank you!

```html
<!DOCTYPE html>
<html lang="en">
<head>
<meta charset="utf-8">
<title>BDN Ltd — Stationery</title>
<link rel="stylesheet" href="https://fonts.googleapis.com/css2?family=Montserrat:wght@400;500;600&family=Playfair+Display:wght@600;700&display=swap">
<style>
:root{
  --navy:#243a80;
  --gold:#b3922b;
  --paper:#f7f7f8;
  --ink:#3a3a3a;
  --muted:#8a8a8a;
  --bg-cards:#ebe9e6;
  --bg-letter:#e7e7e9;
  --bg-env:#ededef;
}
*{box-sizing:border-box;margin:0;padding:0}
html,body{width:1200px;height:2589px;overflow:hidden}
body{position:relative;font-family:"Montserrat",sans-serif;color:var(--ink)}
.section{position:absolute;left:0;width:1200px}
.section--cards{top:0;height:975px;background:var(--bg-cards)}
.section--letter{top:975px;height:815px;background:var(--bg-letter)}
.section--envelopes{top:1790px;height:799px;background:var(--bg-env)}
.sheet{position:absolute;background:var(--paper);box-shadow:0 6px 18px rgba(0,0,0,.12);overflow:hidden}
.brand{font-family:"Playfair Display",serif;font-weight:700;color:var(--navy);white-space:nowrap;line-height:1}
.brand--light{color:#fff}
.stripe{position:absolute;left:0;right:0;bottom:0;display:flex}
.stripe__navy{background:var(--navy);flex:0 0 58%}
.stripe__gold{background:var(--gold);flex:1}
.person{font-family:"Playfair Display",serif;font-weight:700;color:var(--navy);text-transform:uppercase}
.role{font-weight:600;color:var(--gold)}
.contact{list-style:none;color:var(--ink)}
.contact li{display:flex;align-items:center}
.contact svg{flex:none;fill:var(--navy)}
.address{color:var(--ink)}

/* business cards */
.card{width:520px;height:297px}
.card--back{left:150px;top:130px;background:var(--navy)}
.card--back .brand{position:absolute;left:0;right:0;top:122px;text-align:center;font-size:52px}
.card--front{left:530px;top:520px}
.card--front .brand{position:absolute;right:46px;top:46px;font-size:44px}
.card--front .person{position:absolute;left:40px;top:150px;font-size:21px}
.card--front .role{position:absolute;left:40px;top:178px;font-size:17px}
.card--front .contact{position:absolute;left:40px;top:208px;font-size:15px;line-height:22px}
.card--front .contact svg{width:13px;height:13px;margin-right:8px}
.card--front .address{position:absolute;right:40px;top:185px;font-size:16px;line-height:22px;text-align:right}
.card .stripe{height:9px}

/* letterhead */
.letterhead{left:120px;top:45px;width:540px;height:740px}
.letterhead .brand{position:absolute;left:44px;top:46px;font-size:38px}
.letterhead .head-info{position:absolute;right:44px;top:120px;text-align:right;font-size:10.5px;line-height:14px}
.letterhead .head-info .contact li{justify-content:flex-end}
.letterhead .head-info svg{width:9px;height:9px;margin-right:5px}
.letter-body{position:absolute;left:44px;right:44px;top:210px;font-size:9.5px;line-height:14px;color:#6a6a6a}
.letter-body p{margin-bottom:12px}
.signature{width:70px;height:30px;background:#e2e2e4;margin:6px 0 0}
.letterhead .stripe{height:10px}

.mini-card{width:300px;height:171px}
.mini-card--front{left:790px;top:420px}
.mini-card--front .brand{position:absolute;right:24px;top:28px;font-size:24px}
.mini-card--front .person{position:absolute;left:22px;top:68px;font-size:11.5px}
.mini-card--front .role{position:absolute;left:22px;top:84px;font-size:9.5px}
.mini-card--front .contact{position:absolute;left:22px;top:100px;font-size:8.5px;line-height:12px}
.mini-card--front .contact svg{width:8px;height:8px;margin-right:5px}
.mini-card--front .address{position:absolute;right:22px;top:104px;font-size:9px;line-height:12px;text-align:right}
.mini-card .stripe{height:6px}
.mini-card--back{left:700px;top:610px;background:var(--navy)}
.mini-card--back .brand{position:absolute;left:0;right:0;top:68px;text-align:center;font-size:30px}

/* envelopes */
.envelope{width:800px;height:340px}
.envelope--back{left:170px;top:30px}
.envelope__flap{position:absolute;left:0;right:0;top:0;height:130px;background:var(--navy);border-radius:0 0 60px 40px}
.envelope--back .brand{position:absolute;left:0;right:0;top:48px;text-align:center;font-size:38px}
.envelope--front{left:130px;top:410px}
.envelope--front .brand{position:absolute;left:60px;top:50px;font-size:42px}
.envelope--front .address{position:absolute;left:60px;top:170px;font-size:16px;line-height:21px}
.envelope--front .contact{position:absolute;left:60px;top:215px;font-size:16px;line-height:21px}
.envelope--front .contact svg{width:13px;height:13px;margin-right:8px}
.envelope .stripe{height:14px}
</style>
</head>
<body>
<svg width="0" height="0" style="position:absolute" aria-hidden="true">
  <defs>
    <symbol id="icon-phone" viewBox="0 0 24 24"><path d="M6.6 10.8a15.1 15.1 0 0 0 6.6 6.6l2.2-2.2c.3-.3.7-.4 1-.2 1.1.4 2.3.6 3.6.6.6 0 1 .4 1 1V20c0 .6-.4 1-1 1A17 17 0 0 1 3 4c0-.6.4-1 1-1h3.5c.6 0 1 .4 1 1 0 1.3.2 2.5.6 3.6.1.3 0 .7-.2 1z"/></symbol>
    <symbol id="icon-mail" viewBox="0 0 24 24"><path d="M2 5h20v14H2zm2 2v.5l8 5 8-5V7l-8 5z"/></symbol>
    <symbol id="icon-web" viewBox="0 0 24 24"><circle cx="12" cy="12" r="10"/></symbol>
  </defs>
</svg>

<section class="section section--cards">
  <div class="sheet card card--back">
    <div class="brand brand--light">BDN Ltd</div>
  </div>
  <div class="sheet card card--front">
    <div class="brand">BDN Ltd</div>
    <div class="person">Adam Carter</div>
    <div class="role">Director</div>
    <ul class="contact">
      <li><svg><use href="#icon-phone"/></svg>020.555.0148</li>
      <li><svg><use href="#icon-mail"/></svg>info@bdnltd.com</li>
      <li><svg><use href="#icon-web"/></svg>www.bdnltd.com</li>
    </ul>
    <div class="address">Marlow House, 12<br>Hill Street, London</div>
    <div class="stripe"><span class="stripe__navy"></span><span class="stripe__gold"></span></div>
  </div>
</section>

<section class="section section--letter">
  <div class="sheet letterhead">
    <div class="brand">BDN Ltd</div>
    <div class="head-info">
      <div class="address">Marlow House, 12<br>Hill Street, London</div>
      <ul class="contact">
        <li><svg><use href="#icon-phone"/></svg>020.555.0148</li>
        <li><svg><use href="#icon-mail"/></svg>info@bdnltd.com</li>
        <li><svg><use href="#icon-web"/></svg>www.bdnltd.com</li>
      </ul>
    </div>
    <div class="letter-body">
      <p>Dear customer,</p>
      <p>Lorem ipsum dolor sit amet, consectetur adipisicing elit, sed do eiusmod tempor incididunt ut labore et dolore magna aliqua. Ut enim ad minim veniam, quis nostrud exercitation ullamco laboris nisi ut aliquip ex ea commodo consequat. Duis aute irure dolor in reprehenderit in voluptate velit esse cillum dolore eu fugiat nulla pariatur. Excepteur sint occaecat cupidatat non proident, sunt in culpa qui officia deserunt mollit anim id est laborum.</p>
      <p>Lorem ipsum dolor sit amet, consectetur adipisicing elit, sed do eiusmod tempor incididunt ut labore et dolore magna aliqua. Ut enim ad minim veniam, quis nostrud exercitation ullamco laboris nisi ut aliquip ex ea commodo consequat. Duis aute irure dolor in reprehenderit in voluptate velit esse cillum dolore eu fugiat nulla pariatur. Excepteur sint occaecat cupidatat non proident, sunt in culpa qui officia deserunt mollit anim id est laborum.</p>
      <p>Lorem ipsum dolor sit amet, consectetur adipisicing elit, sed do eiusmod tempor incididunt ut labore et dolore magna aliqua. Ut enim ad minim veniam, quis nostrud exercitation ullamco laboris nisi ut aliquip ex ea commodo consequat. Duis aute irure dolor in reprehenderit in voluptate velit esse cillum dolore eu fugiat nulla pariatur. Excepteur sint occaecat cupidatat non proident, sunt in culpa qui officia deserunt mollit anim id est laborum.</p>
      <p>Lorem ipsum dolor sit amet, consectetur adipisicing elit, sed do eiusmod tempor incididunt ut labore et dolore magna aliqua. Ut enim ad minim veniam, quis nostrud exercitation ullamco laboris nisi ut aliquip ex ea commodo consequat. Duis aute irure dolor in reprehenderit.</p>
      <p>Yours Sincerely,</p>
      <div class="signature" role="img" aria-label="Handwritten signature"></div>
    </div>
    <div class="stripe"><span class="stripe__navy"></span><span class="stripe__gold"></span></div>
  </div>

  <div class="sheet mini-card mini-card--front">
    <div class="brand">BDN Ltd</div>
    <div class="person">Adam Carter</div>
    <div class="role">Director</div>
    <ul class="contact">
      <li><svg><use href="#icon-phone"/></svg>020.555.0148</li>
      <li><svg><use href="#icon-mail"/></svg>info@bdnltd.com</li>
      <li><svg><use href="#icon-web"/></svg>www.bdnltd.com</li>
    </ul>
    <div class="address">Marlow House, 12<br>Hill Street, London</div>
    <div class="stripe"><span class="stripe__navy"></span><span class="stripe__gold"></span></div>
  </div>
  <div class="sheet mini-card mini-card--back">
    <div class="brand brand--light">BDN Ltd</div>
  </div>
</section>

<section class="section section--envelopes">
  <div class="sheet envelope envelope--back">
    <div class="envelope__flap"></div>
    <div class="brand brand--light">BDN Ltd</div>
  </div>
  <div class="sheet envelope envelope--front">
    <div class="brand">BDN Ltd</div>
    <div class="address">Marlow House, 12<br>Hill Street, London</div>
    <ul class="contact" style="top:215px">
      <li><svg><use href="#icon-phone"/></svg>020.555.0148</li>
      <li><svg><use href="#icon-mail"/></svg>info@bdnltd.com</li>
      <li><svg><use href="#icon-web"/></svg>www.bdnltd.com</li>
    </ul>
    <div class="stripe"><span class="stripe__navy"></span><span class="stripe__gold"></span></div>
  </div>
</section>
</body>
</html>
```